Company Website Re-design for Software development consultancy

We would like our company website to be redesigned using our existing marketing collateral and website content as a guide

current site : www.brovalex.com.au

For the different pages types and content please base on the following site : https://www.quorvantic.net/

We want a coded site - but will replace the content ourselves within the sections you provide to customise to our needs.

Target Market(s)

Medium to Large corporates needing software design and development services

Industry/Entity Type

Information Technology

Coding

Coded - Design and coding required

Number of Pages Required

5+ page

Font styles to use
Sans Serif

Colors
ec1f27
ffffff
000000

Requirements
Must have
• Align to colour scheme of existing collateral
• Include pages for the key areas of our busines - see : https://www.quorvantic.net/
Nice to have
• image rotators - make the site interesting to the business visitor

```html
<!DOCTYPE html>
<html lang="en">
<head>
<meta charset="utf-8">
<title>Brovalex — Software Development Consultancy</title>
<link rel="stylesheet" href="https://fonts.googleapis.com/css2?family=Poppins:wght@400;500;600;700&family=Open+Sans:ital,wght@0,400;0,600;1,400&display=swap">
<style>
:root{
  --red:#ec1f27;
  --red-deep:#b3121a;
  --black:#000000;
  --ink:#1b1b1b;
  --dark:#232323;
  --white:#ffffff;
  --grey-bg:#ebebeb;
  --text-grey:#666666;
  --line:#d6d6d6;
}
*{margin:0;padding:0;box-sizing:border-box}
html,body{width:1200px;height:3830px;overflow:hidden}
body{font-family:"Open Sans",Arial,sans-serif;color:var(--ink);background:var(--white);position:relative}
.section{position:absolute;left:0;width:1200px;overflow:hidden}
.abs{position:absolute}
h2,h3,.nav,.btn,.name{font-family:"Poppins",Arial,sans-serif}

/* HERO */
.hero{top:0;height:664px;background:linear-gradient(160deg,#3b3b3d 0%,#222 45%,#151515 100%)}
.hero-photo{position:absolute;inset:0;background:radial-gradient(ellipse at 60% 55%,rgba(120,120,125,.35),rgba(0,0,0,.1) 60%),linear-gradient(90deg,rgba(90,70,60,.35),rgba(30,30,35,.2) 50%,rgba(80,60,50,.3))}
.brand{left:184px;top:30px;font-family:"Poppins",sans-serif;font-weight:700;font-size:36px;color:var(--white);letter-spacing:1px}
.nav{left:482px;top:42px;display:flex;gap:34px;font-size:15px;font-weight:500;color:var(--white);text-transform:uppercase}
.hero-title{left:0;width:1200px;top:312px;text-align:center;color:var(--white);font-family:"Poppins",sans-serif;font-weight:600;font-size:37px;line-height:47px;text-transform:uppercase}
.btn{display:inline-block;text-transform:uppercase;font-weight:600;text-align:center}
.btn-solid{background:var(--red);color:var(--white)}
.hero-btn{left:500px;top:429px;width:190px;height:46px;line-height:46px;font-size:18px}
.arrow{top:296px;width:40px;height:60px}

/* WHAT WE DO */
.what{top:664px;height:480px}
.what-art{left:128px;top:26px;width:447px;height:408px;border-radius:50%;background:radial-gradient(circle,#e8eef6 0%,#f5f7fb 55%,#ffffff 72%)}
.what-h{left:613px;top:100px;font-size:31px;font-weight:700;color:var(--black)}
.what-lead{left:613px;top:152px;width:410px;font-size:16px;line-height:25px;color:var(--ink);font-weight:600}
.what-body{left:613px;top:210px;width:410px;font-size:14px;line-height:24px;color:var(--text-grey)}
.btn-outline{border:2px solid var(--red);color:var(--black)}
.what-btn{left:613px;top:342px;width:160px;height:43px;line-height:39px;font-size:15px}

/* SERVICES */
.services{top:1110px;height:620px}
.services h2,.testimonials h2,.team h2,.blog h2{position:absolute;left:0;width:1200px;text-align:center;font-size:29px;font-weight:700}
.services h2{top:100px;color:var(--white)}
.svc{top:200px;width:300px;color:var(--white)}
.svc svg{display:block}
.svc h3{margin-top:18px;font-size:20px;line-height:27px;font-weight:600;text-transform:uppercase}
.svc h3::after{content:"";display:block;width:40px;height:3px;background:var(--white);margin-top:6px}
.svc p{margin-top:18px;font-size:13.5px;line-height:22px;color:#ffdede;width:270px}
.svc .btn{margin-top:20px;width:128px;height:34px;line-height:30px;border:2px solid var(--white);font-size:12px;color:var(--white)}

/* TESTIMONIALS */
.testimonials{top:1680px;height:470px}
.testimonials h2{top:75px;color:var(--white);font-size:28px}
.badge{left:540px;top:146px;width:120px;height:46px;background:#8a8a8a;border-radius:4px}
.quote{left:270px;top:200px;width:660px;text-align:center;color:var(--white);font-style:italic;font-size:20px;line-height:31px}
.qmark{font-family:Georgia,serif;font-style:normal;font-size:70px;line-height:0;vertical-align:-22px;font-weight:700}
.company{left:0;width:1200px;top:305px;text-align:center;color:var(--white);font-family:"Poppins",sans-serif;font-size:15px;font-weight:600}

/* TEAM */
.team{top:2120px;height:520px;background:var(--white)}
.team h2{top:46px;color:var(--red);font-size:28px}
.member{top:110px;width:300px;text-align:center}
.avatar{width:196px;height:196px;border-radius:50%;margin:0 auto;border:3px solid #e2e2e2;background:linear-gradient(180deg,#b9b2ab 0%,#8d8680 55%,#3d4250 100%)}
.member .name{margin-top:14px;font-size:20px;font-weight:700;color:var(--black)}
.member .role{font-size:13px;color:var(--ink);text-transform:uppercase;letter-spacing:.5px}
.member .desc{font-size:15px;line-height:19px;color:var(--ink);width:230px;margin:2px auto 0}

/* BLOG */
.blog{top:2620px;height:560px;background:var(--grey-bg)}
.blog h2{top:60px;color:var(--black);font-size:28px}
.card{background:var(--white);border:1px solid var(--line)}
.card-big{left:191px;top:127px;width:389px;height:342px}
.card-big .img{height:169px;background:linear-gradient(135deg,#cfd4da,#7d8690 60%,#4b545c)}
.date-tag{position:absolute;left:0;top:148px;background:var(--red);color:var(--white);font-size:15px;padding:4px 14px 4px 16px;font-weight:600}
.card-big h3{margin:26px 0 0 26px;font-size:19px;font-weight:600;color:var(--black)}
.card-big p{margin:8px 26px 0;font-size:11px;line-height:15px;color:var(--text-grey)}
.card-big .btn{position:absolute;left:26px;bottom:24px;width:108px;height:28px;line-height:28px;font-size:12px}
.card-small{left:592px;width:429px;height:165px}
.card-small .img{position:absolute;left:0;top:0;width:208px;height:100%;background:linear-gradient(135deg,#1e2a3c,#3a4b66 55%,#182030)}
.card-small .meta{position:absolute;left:230px;top:20px;font-size:12px;color:var(--text-grey)}
.card-small h3{position:absolute;left:230px;top:40px;font-size:16px;font-weight:600;color:var(--black)}
.card-small p{position:absolute;left:230px;top:70px;width:180px;font-size:10px;line-height:13px;color:var(--text-grey)}
.card-small .btn{position:absolute;left:230px;top:124px;width:100px;height:25px;line-height:25px;font-size:11px}

/* CONTACT */
.contact{top:3150px;height:605px;background:linear-gradient(180deg,#262626,#141414)}
.form{left:166px;top:105px;width:421px;height:370px;background:var(--red);padding:36px 38px 0}
.field{color:var(--white);font-size:14px;text-transform:uppercase;border-bottom:1.5px solid var(--white);height:31px;line-height:24px;width:344px;margin-bottom:19px}
.field.msg{height:74px}
.submit{width:166px;height:47px;line-height:47px;background:var(--black);color:var(--white);font-size:19px;margin-top:8px}
.info{left:682px;top:110px;color:var(--white)}
.info h2{font-size:31px;font-weight:700;margin-bottom:22px}
.info .label{font-size:14px;font-weight:600;text-transform:uppercase;font-family:"Poppins",sans-serif}
.info .val{font-size:16px;text-transform:uppercase;margin-bottom:22px}
.socials{display:flex;gap:26px;margin-top:10px}
.socials span{width:20px;height:20px;border-radius:50%;background:var(--white)}

/* FOOTER */
.footer{top:3755px;height:75px;background:var(--white);text-align:center;font-size:15px;line-height:75px;color:var(--ink)}
</style>
</head>
<body>

<header class="section hero">
  <div class="hero-photo" role="img" aria-label="Photo of a busy open-plan software office with developers at laptops"></div>
  <div class="abs" style="inset:0;background:rgba(0,0,0,.35)"></div>
  <div class="abs brand">BROVALEX</div>
  <nav class="abs nav"><span>About us</span><span>Services</span><span>Solutions</span><span>Testimonial</span><span>Contact</span></nav>
  <h1 class="abs hero-title">Software development consultancy<br>building software better</h1>
  <a class="abs btn btn-solid hero-btn">Get started</a>
  <svg class="abs arrow" style="left:98px" viewBox="0 0 40 60"><polyline points="30,6 10,30 30,54" fill="none" stroke="#fff" stroke-width="4"/></svg>
  <svg class="abs arrow" style="left:1066px" viewBox="0 0 40 60"><polyline points="10,6 30,30 10,54" fill="none" stroke="#fff" stroke-width="4"/></svg>
</header>

<section class="section what">
  <div class="abs what-art" role="img" aria-label="Illustration of a laptop showing code surrounded by tool, gear, cloud and database icons"></div>
  <h2 class="abs what-h">WHAT WE DO</h2>
  <p class="abs what-lead">Integer congue augue et malesuada iaculis ipsum dui aliquet felis at cursus magna nisl nec elit</p>
  <p class="abs what-body">Altricies sit amet porttitor mattis enim In massa libero interdum nec interdum vel blandit sed nulla In ullamcorper est eget tempor cursus neque mi consectetuer mi a ultricies massa est sed nisl Class aptent taciti sociosqu ad litora</p>
  <a class="abs btn btn-outline what-btn">Read more</a>
</section>

<section class="section services">
  <svg class="abs" style="left:0;top:0" width="1200" height="620" viewBox="0 0 1200 620">
    <defs><linearGradient id="svcRed" x1="0" y1="0" x2="1" y2="1"><stop offset="0" stop-color="#ef3a32"/><stop offset="1" stop-color="#a50f16"/></linearGradient></defs>
    <polygon points="0,0 1200,64 1200,570 0,620" fill="url(#svcRed)"/>
    <polygon points="980,52 1200,30 1200,64" fill="#1a1a1a"/>
    <polygon points="0,0 980,52 1200,64" fill="#ffffff"/>
  </svg>
  <h2>OUR SERVICES</h2>
  <div class="abs svc" style="left:197px">
    <svg width="70" height="66" viewBox="0 0 70 66" fill="none" stroke="#fff" stroke-width="2.5"><rect x="4" y="4" width="62" height="48" rx="3"/><line x1="4" y1="14" x2="66" y2="14"/><polyline points="26,26 20,33 26,40"/><polyline points="44,26 50,33 44,40"/><line x1="37" y1="24" x2="33" y2="42"/><line x1="20" y1="60" x2="50" y2="60"/></svg>
    <h3>Software<br>Development</h3>
    <p>Ais enim In massa libero interdum nec interdum vel blandit sed nulla In ullamcorper est eget tempor cursus neque mi consectetuer mi</p>
    <a class="btn">Read more</a>
  </div>
  <div class="abs svc" style="left:490px">
    <svg width="70" height="66" viewBox="0 0 70 66" fill="none" stroke="#fff" stroke-width="2.5"><rect x="18" y="2" width="34" height="62" rx="4"/><line x1="18" y1="12" x2="52" y2="12"/><line x1="18" y1="54" x2="52" y2="54"/><rect x="25" y="19" width="9" height="9"/><rect x="37" y="19" width="9" height="9"/><rect x="25" y="32" width="9" height="9"/><rect x="37" y="32" width="9" height="9"/></svg>
    <h3>Mobile App<br>Development</h3>
    <p>Ais enim In massa libero interdum nec interdum vel blandit sed nulla In ullamcorper est eget tempor cursus neque mi consectetuer mi</p>
    <a class="btn">Read more</a>
  </div>
  <div class="abs svc" style="left:784px">
    <svg width="70" height="66" viewBox="0 0 70 66" fill="none" stroke="#fff" stroke-width="2.5"><circle cx="35" cy="30" r="16"/><circle cx="35" cy="30" r="6"/><line x1="35" y1="6" x2="35" y2="12"/><line x1="35" y1="48" x2="35" y2="54"/><line x1="11" y1="30" x2="17" y2="30"/><line x1="53" y1="30" x2="59" y2="30"/><line x1="28" y1="54" x2="42" y2="54"/><line x1="30" y1="60" x2="40" y2="60"/></svg>
    <h3>IT Consulting<br>Services</h3>
    <p>Ais enim In massa libero interdum nec interdum vel blandit sed nulla In ullamcorper est eget tempor cursus neque mi consectetuer mi</p>
    <a class="btn">Read more</a>
  </div>
</section>

<section class="section testimonials" style="background:linear-gradient(180deg,#1d1d1d,#262626)">
  <div class="abs" style="inset:0;background:radial-gradient(ellipse at 80% 40%,rgba(90,90,100,.35),transparent 60%)" role="img" aria-label="Darkened photo of a developer working at a computer"></div>
  <h2>TESTIMONIALS</h2>
  <div class="abs badge"></div>
  <p class="abs quote"><span class="qmark">“</span> Aorbi porta libero id ullamcorper nonummy nibh ligula pulvinar metus eget consectetuer augue nisi quis locus Ut ac mi quis locus mollis aliquam vvscelerisque mi tortor at ipsum <span class="qmark">”</span></p>
  <div class="abs company">COMPANY NAME</div>
  <svg class="abs arrow" style="left:182px;top:176px" viewBox="0 0 40 60"><polyline points="28,8 10,30 28,52" fill="none" stroke="#888" stroke-width="3"/></svg>
  <svg class="abs arrow" style="left:978px;top:176px" viewBox="0 0 40 60"><polyline points="12,8 30,30 12,52" fill="none" stroke="#888" stroke-width="3"/></svg>
  <svg class="abs" style="left:0;top:380px" width="1200" height="90" viewBox="0 0 1200 90"><polygon points="700,45 1200,5 1200,22" fill="#ec1f27"/><polygon points="0,90 1200,10 1200,90" fill="#ffffff"/></svg>
</section>

<section class="section team">
  <h2>OUR TEAM</h2>
  <div class="abs member" style="left:140px"><div class="avatar" role="img" aria-label="Portrait photo of a partner"></div><div class="name">Marcus Tellan</div><div class="role">Partner</div><div class="desc">Marcus's one of the best developers on the planet</div></div>
  <div class="abs member" style="left:446px"><div class="avatar" role="img" aria-label="Portrait photo of a partner"></div><div class="name">Owen Pridell</div><div class="role">Partner</div><div class="desc">Owen's been running software projects for 20 years</div></div>
  <div class="abs member" style="left:752px"><div class="avatar" role="img" aria-label="Portrait photo of a partner"></div><div class="name">Lucas Brenvik</div><div class="role">Partner</div><div class="desc">Lucas codes for fun as much as he does for work</div></div>
  <svg class="abs" style="left:0;top:440px" width="1200" height="80" viewBox="0 0 1200 80"><polygon points="0,40 1200,80 0,80" fill="#ebebeb"/><polygon points="880,70 1200,40 1200,80 1100,80" fill="#ec1f27"/><polygon points="1000,72 1200,55 1200,80" fill="#8a0c11"/></svg>
</section>

<section class="section blog">
  <h2>OUR BLOG</h2>
  <article class="abs card card-big">
    <div class="img" role="img" aria-label="Photo of two colleagues reviewing work on a laptop"></div>
    <span class="date-tag">10 SEP 2018</span>
    <h3>Maecenas at justo id velit placerat</h3>
    <p>netus et malesuada fames ac turpis egestas Cras id elit integer quis urna Ut ante enim dapibus malesuada fringilla eu condimen</p>
    <a class="btn btn-solid">Read more</a>
  </article>
  <article class="abs card card-small" style="top:127px">
    <div class="img" role="img" aria-label="Photo of code on a monitor"></div>
    <div class="meta">04 SEP 2018</div>
    <h3>News Title here</h3>
    <p>netus et malesuada fames ac turpis egestas Cras id elit integer quis urna Ut ante enim dapibus malesuada</p>
    <a class="btn btn-solid">Read more</a>
  </article>
  <article class="abs card card-small" style="top:304px">
    <div class="img" style="background:linear-gradient(135deg,#d9d9d9,#6e6e6e 55%,#2c2c2c)" role="img" aria-label="Photo of a laptop on a desk"></div>
    <div class="meta">09 SEP 2018</div>
    <h3>News Title here</h3>
    <p>netus et malesuada fames ac turpis egestas Cras id elit integer quis urna Ut ante enim dapibus malesuada</p>
    <a class="btn btn-solid">Read more</a>
  </article>
  <svg class="abs" style="left:0;top:500px" width="1200" height="60" viewBox="0 0 1200 60"><polygon points="0,30 1200,60 0,60" fill="#262626"/><polygon points="0,10 330,40 0,55" fill="#ec1f27"/></svg>
</section>

<section class="section contact">
  <div class="abs" style="inset:0;background:radial-gradient(ellipse at 30% 30%,rgba(80,80,80,.35),transparent 60%)" role="img" aria-label="Darkened photo of an office workspace"></div>
  <form class="abs form">
    <div class="field">Name</div>
    <div class="field">Email</div>
    <div class="field">Phone number</div>
    <div class="field msg">Message</div>
    <div class="btn submit">Submit</div>
  </form>
  <div class="abs info">
    <h2>CONTACT US</h2>
    <div class="label">Address</div><div class="val">42 - 44 Harlow Lane, Sydney 2000</div>
    <div class="label">Phone number</div><div class="val">(02) 5550 1837</div>
    <div class="label">Email us</div><div class="val">info@brovalex.com.au</div>
    <div class="label">Follow us</div>
    <div class="socials"><span></span><span></span><span></span><span></span></div>
  </div>
</section>

<footer class="section footer">© 2018 Company Name &nbsp;All right reserved &nbsp;Term of Use</footer>

</body>
</html>
```